Buisness card

**Front Side:**

**[Your Company Logo]**
**Steadfast Upkeep Engineering**
*Keeping Your Equipment Running Smoothly*

**Contact Information:**
- **Name:** [dale Harwick
- **Title:** [owner
- **Phone:** [5073918246
- **Email:** dale@suevx.com

**Back Side:**

**Services Offered:**
- Routine Inspections
- Equipment Maintenance
- Emergency Repairs
- Consultation Services
- New installs
Tag line
Be proactive not reactive

```html
<!DOCTYPE html>
<html lang="en">
<head>
<meta charset="utf-8">
<title>Steadfast Upkeep Engineering – Business Card</title>
<link href="https://fonts.googleapis.com/css2?family=Open+Sans:ital,wght@0,400;0,600;0,700;0,800;1,700;1,800&display=swap" rel="stylesheet">
<style>
  :root {
    --navy: #022a72;
    --royal: #0a6cff;
    --cyan: #12c5f5;
    --ink: #111111;
    --grey: #5a5a5a;
    --paper: #ffffff;
    --backdrop: #2a2a2a;
  }
  * { box-sizing: border-box; margin: 0; padding: 0; }
  html, body {
    width: 1200px; height: 900px; overflow: hidden;
    background: var(--backdrop);
    font-family: "Open Sans", sans-serif;
  }
  .sheet {
    width: 1200px; height: 900px;
    display: flex; flex-direction: column; align-items: center; justify-content: center;
    gap: 40px;
  }
  .card {
    position: relative;
    width: 700px; height: 400px;
    background: var(--paper);
    overflow: hidden;
    box-shadow: 0 10px 30px rgba(0,0,0,.5);
  }

  /* front */
  .front-waves { position: absolute; inset: 0; }
  .brand {
    position: absolute; left: 60px; top: 36px;
    display: flex; align-items: center; gap: 22px;
  }
  .brand-dot {
    width: 104px; height: 104px; border-radius: 50%;
    background: var(--navy);
    flex: none;
  }
  .brand-name {
    font-weight: 800; font-size: 34px; line-height: 1.05;
    color: var(--navy);
  }
  .brand-tagline {
    margin-top: 8px;
    font-weight: 700; font-size: 15px; letter-spacing: .5px;
    color: var(--ink); text-transform: uppercase;
  }
  .contact-block {
    position: absolute; left: 60px; bottom: 60px;
    display: flex; align-items: center; gap: 22px;
  }
  .person { text-align: right; }
  .person-name { font-weight: 700; font-size: 30px; color: var(--cyan); }
  .person-title { font-size: 18px; color: var(--paper); }
  .divider-v { width: 1px; height: 70px; background: rgba(255,255,255,.7); }
  .contact-list { list-style: none; color: var(--paper); font-size: 19px; line-height: 1.5; }
  .contact-list li { display: flex; align-items: center; gap: 8px; }
  .contact-list svg { width: 16px; height: 16px; fill: var(--cyan); }

  /* back */
  .back-brand {
    position: absolute; left: 40px; top: 50px; width: 290px;
    display: flex; flex-direction: column; align-items: center; gap: 16px;
    text-align: center;
  }
  .back-brand .brand-dot { width: 150px; height: 150px; }
  .back-brand .brand-name { font-size: 24px; }
  .back-tagline {
    position: absolute; left: 40px; bottom: 40px; width: 300px;
    font-weight: 800; font-style: italic; font-size: 19px; color: var(--grey);
    text-align: center;
  }
  .back-divider {
    position: absolute; left: 360px; top: 70px; width: 1px; height: 200px;
    background: var(--grey);
  }
  .services { position: absolute; left: 390px; top: 80px; }
  .services-title { font-weight: 700; font-size: 24px; color: var(--cyan); margin-bottom: 4px; }
  .services-list { list-style: none; font-size: 19px; color: var(--grey); line-height: 1.35; }
  .services-list li::before {
    content: ""; display: inline-block; width: 7px; height: 7px; border-radius: 50%;
    background: var(--cyan); margin-right: 8px; vertical-align: middle;
  }
</style>
</head>
<body>
<main class="sheet">

  <section class="card card-front" aria-label="Card front">
    <svg class="front-waves" viewBox="0 0 700 400" preserveAspectRatio="none" aria-hidden="true">
      <path d="M0 185 Q420 200 700 395 L700 400 L0 400 Z" fill="var(--cyan)"/>
      <path d="M0 180 Q410 190 680 400 L0 400 Z" fill="var(--paper)"/>
      <path d="M0 170 Q380 175 620 400 L0 400 Z" fill="var(--royal)"/>
      <path d="M0 185 Q370 190 600 400 L0 400 Z" fill="var(--navy)"/>
      <path d="M190 196 Q450 230 560 320" stroke="var(--cyan)" stroke-width="2" fill="none"/>
    </svg>

    <div class="brand">
      <div class="brand-dot"></div>
      <div>
        <div class="brand-name">Steadfast Upkeep<br>Engineering</div>
        <div class="brand-tagline">Be proactive not reactive</div>
      </div>
    </div>

    <div class="contact-block">
      <div class="person">
        <div class="person-name">dale Harwick</div>
        <div class="person-title">owner</div>
      </div>
      <div class="divider-v"></div>
      <ul class="contact-list">
        <li>
          <svg viewBox="0 0 24 24"><path d="M6.6 10.8a15 15 0 0 0 6.6 6.6l2.2-2.2a1 1 0 0 1 1-.25 11.4 11.4 0 0 0 3.6.6 1 1 0 0 1 1 1V20a1 1 0 0 1-1 1A17 17 0 0 1 3 4a1 1 0 0 1 1-1h3.5a1 1 0 0 1 1 1c0 1.25.2 2.45.6 3.6a1 1 0 0 1-.25 1z"/></svg>
          5073918246
        </li>
        <li>
          <svg viewBox="0 0 24 24"><path d="M3 5h18v14H3z M3 5l9 7 9-7" fill="none" stroke="var(--cyan)" stroke-width="2"/></svg>
          dale@suevx.com
        </li>
      </ul>
    </div>
  </section>

  <section class="card card-back" aria-label="Card back">
    <div class="back-brand">
      <div class="brand-dot"></div>
      <div class="brand-name">Steadfast Upkeep Engineering</div>
    </div>
    <div class="back-tagline">Be proactive not reactive</div>
    <div class="back-divider"></div>
    <div class="services">
      <h2 class="services-title">Services Offered:</h2>
      <ul class="services-list">
        <li>Routine Inspections</li>
        <li>Equipment Maintenance</li>
        <li>Emergency Repairs</li>
        <li>Consultation Services</li>
        <li>New installs</li>
      </ul>
    </div>
  </section>

</main>
</body>
</html>
```